Use new branding for Orvel website

Orvel is a medical supplier of fitted socks for patients. Unlike a regular sock you receive upon admission that is slippery and prone to falling, Orvel unique factor is it’s gripping material which gives one traction while walking.
We would like to incorporate the new logo and branding into the Orvel website. The copy should stay the same. The logos in various formats and brand guidelines are included in the attachments. While the logos have a black or white background, you may use other colors if it integrates well with your design. Please submit your designs in either Wix or Squarespace
Hello all - additional information. We would like the design submission in either Wix or Squarespace.
Number of Pages Required
1 page

```html
<!DOCTYPE html>
<html lang="en">
<head>
<meta charset="utf-8">
<title>Orvel Tech</title>
<link rel="stylesheet" href="https://fonts.googleapis.com/css2?family=Rubik:wght@400;500;600;700&family=Roboto:ital,wght@0,400;0,500;1,400&display=swap">
<style>
:root{
  --yellow:#fcc416;
  --ink:#1d1d1d;
  --text:#555;
  --muted:#8a8a8a;
  --light:#f4f4f4;
  --white:#fff;
  --black:#050505;
}
*{box-sizing:border-box;margin:0;padding:0}
html,body{width:1200px;height:4093px;overflow:hidden}
body{position:relative;background:var(--white);font-family:"Roboto",sans-serif;color:var(--text)}
.abs{position:absolute}
h2,h3{font-family:"Rubik",sans-serif;font-weight:500;color:var(--ink)}
.section-title{position:absolute;left:0;width:1200px;text-align:center;font-size:32px;line-height:38px}
.section-title::after{content:"";display:block;width:72px;height:3px;background:var(--yellow);margin:12px auto 0}

/* header */
.topline{top:0;left:0;width:1200px;height:4px;background:var(--yellow)}
.social-hex{width:46px;height:52px;background:var(--yellow);clip-path:polygon(50% 0,100% 25%,100% 75%,50% 100%,0 75%,0 25%)}
.brand{display:flex;align-items:center;gap:12px}
.brand-mark{width:30px;height:30px;border-radius:50%;background:var(--yellow)}
.brand-name{font-family:"Rubik",sans-serif;font-weight:500;font-size:38px;line-height:44px;letter-spacing:1px;color:var(--ink)}
.phone-badge{top:25px;left:815px;width:48px;height:52px;background:var(--yellow);clip-path:polygon(50% 0,100% 25%,100% 75%,50% 100%,0 75%,0 25%);display:flex;align-items:center;justify-content:center}
.phone-note{top:32px;left:877px;font-size:9px;color:var(--yellow);text-transform:uppercase}
.phone-num{top:48px;left:877px;font-family:"Rubik",sans-serif;font-size:19px;color:var(--ink)}
.nav{position:absolute;top:105px;left:0;width:1200px;height:65px;z-index:3}
.navbar{position:absolute;top:0;left:95px;width:1010px;height:65px;background:var(--yellow);clip-path:polygon(0 0,100% 0,97.5% 100%,2.5% 100%)}
.nav-item{position:absolute;top:25px;font-family:"Rubik",sans-serif;font-weight:500;font-size:13px;color:var(--ink)}
.login{position:absolute;top:9px;left:850px;width:160px;height:48px;border-radius:24px;background:var(--white);display:flex;align-items:center;gap:16px;padding-left:18px;font-family:"Rubik",sans-serif;font-weight:500;font-size:15px;color:var(--ink);box-shadow:0 2px 6px rgba(0,0,0,.12)}
.btn-dot{width:22px;height:22px;border-radius:50%;border:2px solid var(--ink);flex:none}

/* hero */
.hero{top:140px;left:0;width:1200px;height:605px;background:linear-gradient(120deg,#8f979f 0%,#b3b7bb 35%,#8398b2 68%,#4f6f98 100%)}
.hero-title{top:300px;left:110px;font-family:"Rubik",sans-serif;font-weight:600;font-size:64px;line-height:72px;color:var(--white);z-index:2}
.hero-title em{font-style:normal;color:var(--yellow)}
.hero-text{top:393px;left:110px;width:470px;font-size:13px;line-height:28px;color:var(--white);z-index:2}
.btn-yellow{top:471px;left:110px;width:177px;height:49px;border-radius:25px;background:var(--yellow);display:flex;align-items:center;gap:12px;padding-left:18px;font-family:"Rubik",sans-serif;font-weight:500;font-size:15px;color:var(--ink);box-shadow:0 3px 8px rgba(0,0,0,.2);z-index:2}
.dots{top:676px;left:574px;display:flex;gap:4px;z-index:2}
.dots i{width:8px;height:8px;border-radius:50%;background:var(--white)}
.dots i:first-child{background:var(--yellow)}

/* products */
.round-btn{width:38px;height:38px;border-radius:50%;display:flex;align-items:center;justify-content:center}
.product-card{top:912px;width:216px;height:245px;background:var(--white);box-shadow:0 2px 10px rgba(0,0,0,.13)}
.product-card .photo{position:absolute;inset:0}
.product-name{top:1178px;width:216px;text-align:center;font-family:"Rubik",sans-serif;font-weight:500;font-size:15px;color:var(--ink)}
.stars{top:1200px;width:216px;text-align:center;font-size:12px;letter-spacing:2px;color:var(--yellow)}

/* about */
.about-band{top:1350px;left:0;width:1200px;height:502px;background:var(--yellow)}
.about-photo{top:1350px;left:0;width:600px;height:502px;background:linear-gradient(135deg,#7b8273 0%,#a6a99b 50%,#c4c6c0 100%)}
.about-title{top:1410px;left:663px;font-size:32px;line-height:38px}
.about-title::after{content:"";display:block;width:56px;height:3px;background:var(--ink);margin-top:10px}
.about-text{top:1487px;left:663px;width:470px;font-size:13.5px;line-height:28px;color:#333}
.btn-white{top:1735px;left:663px;width:176px;height:50px;border-radius:25px;background:var(--white);display:flex;align-items:center;gap:12px;padding-left:18px;font-family:"Rubik",sans-serif;font-weight:500;font-size:15px;color:var(--ink);box-shadow:0 3px 8px rgba(0,0,0,.15)}

/* testimonial */
.testi-card{top:2082px;left:241px;width:716px;height:234px;background:var(--white);border-radius:8px;box-shadow:0 2px 12px rgba(0,0,0,.14)}
.avatar{top:2045px;left:562px;width:76px;height:76px;border-radius:50%;background:linear-gradient(180deg,#c9d2de,#2b3c5e);border:3px solid var(--white)}
.testi-name{top:2136px;left:0;width:1200px;text-align:center;font-family:"Rubik",sans-serif;font-size:15px;color:var(--yellow)}
.testi-text{top:2166px;left:285px;width:630px;text-align:center;font-style:italic;font-size:13px;line-height:28px;color:#444}
.arrow-ghost{width:46px;height:46px;border-radius:50%;background:var(--white);box-shadow:0 2px 8px rgba(0,0,0,.18);display:flex;align-items:center;justify-content:center}

/* blog */
.blog-band{top:2397px;left:0;width:1200px;height:640px;background:var(--light)}
.blog-card{top:2557px;width:289px;height:398px;background:var(--white);box-shadow:0 2px 10px rgba(0,0,0,.1)}
.blog-photo{position:absolute;top:5px;left:5px;width:279px;height:191px}
.blog-title{position:absolute;top:225px;left:24px;width:245px;font-size:14px;line-height:24px}
.blog-text{position:absolute;top:275px;left:22px;width:245px;font-size:12px;line-height:19px;color:var(--muted)}
.blog-rule{position:absolute;top:348px;left:22px;width:245px;height:1px;background:#ccc}
.blog-meta{position:absolute;top:370px;left:22px;width:245px;display:flex;justify-content:space-between;font-size:11.5px;color:var(--muted)}
.blog-meta b{font-weight:400;color:var(--yellow)}
.arrow-grey{width:44px;height:44px;border-radius:50%;background:#dcdcdc;display:flex;align-items:center;justify-content:center}

/* partners */
.partner-band{top:3037px;left:0;width:1200px;height:560px;background:var(--yellow)}
.partner-title::after{background:var(--ink)}
.badge{width:127px;height:146px;background:var(--white);clip-path:polygon(50% 0,100% 25%,100% 75%,50% 100%,0 75%,0 25%)}

/* mailing */
.mail-title{top:3632px;left:0;width:1200px;text-align:center;font-size:32px;line-height:38px;color:var(--white)}
.mail-field{top:3705px;left:291px;width:599px;height:48px;border-radius:24px;background:var(--white);padding-left:44px;line-height:48px;font-size:13px;color:#bbb}
.subscribe{top:3707px;left:743px;width:145px;height:44px;border-radius:22px;background:var(--yellow);text-align:center;line-height:44px;font-family:"Rubik",sans-serif;font-weight:500;font-size:15px;color:var(--ink)}
.rule{left:73px;width:1054px;height:1px;background:#555}

/* footer */
.footer-head{top:3822px;font-family:"Rubik",sans-serif;font-weight:500;font-size:15px;color:var(--white)}
.footer-list{top:3854px;list-style:none;font-size:13px;line-height:28px;color:var(--white)}
.footer-list li::before{content:"»";margin-right:10px}
.contact-row{display:flex;gap:12px;font-size:13px;line-height:28px;color:var(--white)}
.contact-row svg{flex:none;margin-top:8px}
.foot-social{top:4016px;display:flex;gap:16px;left:125px}
.foot-social i{width:28px;height:28px;border-radius:50%;background:var(--yellow)}
.copyright{top:4020px;left:0;width:1200px;text-align:center;font-size:12px;color:var(--white)}
.copyright b{font-weight:500;color:var(--yellow)}
</style>
</head>
<body>

<!-- header -->
<div class="abs topline"></div>
<div class="abs social-hex" style="top:25px;left:128px"></div>
<div class="abs social-hex" style="top:25px;left:183px"></div>
<div class="abs social-hex" style="top:25px;left:238px"></div>
<div class="abs brand" style="top:26px;left:478px"><span class="brand-mark"></span><span class="brand-name">ORVEL TECH</span></div>
<div class="abs phone-badge">
  <svg width="18" height="18" viewBox="0 0 24 24"><path fill="#fff" d="M6.6 10.8a15 15 0 0 0 6.6 6.6l2.2-2.2a1 1 0 0 1 1-.25 11.4 11.4 0 0 0 3.6.6 1 1 0 0 1 1 1V20a1 1 0 0 1-1 1A17 17 0 0 1 3 4a1 1 0 0 1 1-1h3.5a1 1 0 0 1 1 1c0 1.25.2 2.45.6 3.6a1 1 0 0 1-.25 1z"/></svg>
</div>
<div class="abs phone-note">Can't find what you are looking for?</div>
<div class="abs phone-num">CALL US 555-210-4477</div>

<!-- hero -->
<div class="abs hero" role="img" aria-label="Photo of a patient's foot in a white grip sock stepping on an exercise mat beside a crutch"></div>
<svg class="abs" style="top:140px;left:0" width="1200" height="605" viewBox="0 0 1200 605">
  <polygon points="0,605 0,555 297,495 600,600 914,495 1200,555 1200,605" fill="#fff"/>
  <polyline points="0,555 297,495 600,600 914,495 1200,555" fill="none" stroke="#fcc416" stroke-width="10"/>
</svg>
<h1 class="abs hero-title">ORVEL <em>TECH</em></h1>
<p class="abs hero-text">Lorem ipsum dolor sit amet, consectetur adipiscing elit, sed do eiusmod tempor incididunt ut labore et dolore magna aliqua.</p>
<div class="abs btn-yellow"><span class="btn-dot"></span>GET STARTED</div>
<div class="abs dots"><i></i><i></i><i></i><i></i><i></i></div>

<nav class="nav">
  <div class="navbar"></div>
  <span class="nav-item" style="left:187px">HOME</span>
  <span class="nav-item" style="left:265px">ABOUT US</span>
  <span class="nav-item" style="left:369px">PRODUCTS</span>
  <span class="nav-item" style="left:478px">REVIEWS</span>
  <span class="nav-item" style="left:578px">BLOG</span>
  <span class="nav-item" style="left:651px">CONTACT US</span>
  <div class="login"><span class="btn-dot"></span>LOGIN</div>
</nav>

<!-- products -->
<h2 class="section-title" style="top:826px">OUR PRODUCTS</h2>
<div class="abs round-btn" style="top:819px;left:980px;border:2px solid var(--yellow)">
  <svg width="10" height="10" viewBox="0 0 10 10"><path d="M6.5 1 2.5 5l4 4" fill="none" stroke="#fcc416" stroke-width="1.6"/></svg>
</div>
<div class="abs round-btn" style="top:819px;left:1029px;background:var(--yellow)">
  <svg width="10" height="10" viewBox="0 0 10 10"><path d="M3.5 1l4 4-4 4" fill="none" stroke="#fff" stroke-width="1.6"/></svg>
</div>

<div class="abs product-card" style="left:132px"><div class="photo" style="background:linear-gradient(180deg,#f6f6f6 0%,#e3e5ea 45%,#3e4a63 100%)" role="img" aria-label="Product photo: navy open-toe grip sock"></div></div>
<div class="abs product-card" style="left:372px"><div class="photo" style="background:linear-gradient(180deg,#f4f4f4 0%,#9a9a9a 40%,#1c1c1c 100%)" role="img" aria-label="Product photo: black knee-high compression socks"></div></div>
<div class="abs product-card" style="left:612px"><div class="photo" style="background:linear-gradient(180deg,#efe2d8 0%,#8e8a88 45%,#181818 100%)" role="img" aria-label="Product photo: black knee-length compression sock"></div></div>
<div class="abs product-card" style="left:853px"><div class="photo" style="background:linear-gradient(180deg,#f1e3d6 0%,#d6b79c 55%,#c29c7c 100%)" role="img" aria-label="Product photo: beige knee-high compression stockings"></div></div>
<div class="abs product-name" style="left:132px">PRODUCT NAME</div>
<div class="abs product-name" style="left:372px">PRODUCT NAME</div>
<div class="abs product-name" style="left:612px">PRODUCT NAME</div>
<div class="abs product-name" style="left:853px">PRODUCT NAME</div>
<div class="abs stars" style="left:132px">★★★★★</div>
<div class="abs stars" style="left:372px">★★★★★</div>
<div class="abs stars" style="left:612px">★★★★★</div>
<div class="abs stars" style="left:853px">★★★★★</div>

<!-- about -->
<div class="abs about-band"></div>
<div class="abs about-photo" role="img" aria-label="Close-up photos of knit socks and fabric textures"></div>
<h2 class="abs about-title">ABOUT ORVEL TECH</h2>
<p class="abs about-text">Lorem ipsum dolor sit amet, consectetur adipiscing elit, sed do eiusmod tempor incididunt ut labore et dolore magna aliqua. Quis ipsum suspendisse ultrices gravida. Risus commodo viverra maecenas accumsan lacus vel facilisis. Sed ut perspiciatis unde omnis iste natus error sit voluptatem accusantium doloremque laudantium, totam rem aperiam, eaque ipsa quae ab illo inventore veritatis et quasi architecto beatae vitae dicta sunt explicabo. Nemo enim ipsam voluptatem quia voluptas sit aspernatur aut odit aut fugit, sed quia.</p>
<div class="abs btn-white"><span class="btn-dot"></span>LEARN MORE</div>

<!-- testimonials -->
<h2 class="section-title" style="top:1966px">OUR CLIENT TESTIMONALS</h2>
<div class="abs testi-card"></div>
<div class="abs avatar" role="img" aria-label="Portrait photo of the client"></div>
<div class="abs testi-name">JOHN DOE</div>
<p class="abs testi-text">Lorem ipsum dolor sit amet, consectetur adipiscing elit, sed do eiusmod tempor incididunt ut labore et dolore magna aliqua. Ut enim ad minim veniam, quis nostrud exercitation ullamco laboris nisi ut aliquip ex ea commodo consequat. Duis aute irure dolor in reprehenderit in voluptate velit esse cillum dolore eu fugiat nulla pariatur. Excepteur sint occaecat cupidatat non proident.</p>
<div class="abs arrow-ghost" style="top:2176px;left:216px"><svg width="10" height="12" viewBox="0 0 10 12"><path d="M7 1 2 6l5 5" fill="none" stroke="#333" stroke-width="1.6"/></svg></div>
<div class="abs arrow-ghost" style="top:2176px;left:937px"><svg width="10" height="12" viewBox="0 0 10 12"><path d="M3 1l5 5-5 5" fill="none" stroke="#333" stroke-width="1.6"/></svg></div>

<!-- blog -->
<div class="abs blog-band"></div>
<h2 class="section-title" style="top:2471px">OUR LATEST BLOG</h2>
<div class="abs arrow-grey" style="top:2745px;left:70px"><svg width="10" height="12" viewBox="0 0 10 12"><path d="M7 1 2 6l5 5" fill="none" stroke="#333" stroke-width="1.6"/></svg></div>
<div class="abs arrow-grey" style="top:2745px;left:1085px"><svg width="10" height="12" viewBox="0 0 10 12"><path d="M3 1l5 5-5 5" fill="none" stroke="#333" stroke-width="1.6"/></svg></div>

<article class="abs blog-card" style="left:143px">
  <div class="blog-photo" style="background:linear-gradient(135deg,#8a9a7c,#d7d9dc)" role="img" aria-label="Photo of feet in white socks resting on a chair outdoors"></div>
  <h3 class="blog-title">CONSECTETUR ADIPISCING ELIT DO EIUSMOD</h3>
  <p class="blog-text">Lorem ipsum dolor sit amet, consectetur adipiscing elit, sed do eiusmod tempor incididunt ut labore et dolore</p>
  <div class="blog-rule"></div>
  <div class="blog-meta"><span>by John doe</span><b>More information</b></div>
</article>
<article class="abs blog-card" style="left:456px">
  <div class="blog-photo" style="background:linear-gradient(135deg,#c9c3c4,#2c3347)" role="img" aria-label="Photo of hands pulling a navy sock onto a foot"></div>
  <h3 class="blog-title">CONSECTETUR ADIPISCING ELIT DO EIUSMOD</h3>
  <p class="blog-text">Lorem ipsum dolor sit amet, consectetur adipiscing elit, sed do eiusmod tempor incididunt ut labore et dolore</p>
  <div class="blog-rule"></div>
  <div class="blog-meta"><span>by John doe</span><b>More information</b></div>
</article>
<article class="abs blog-card" style="left:768px">
  <div class="blog-photo" style="background:linear-gradient(135deg,#b7c2cc,#d9cfc6)" role="img" aria-label="Photo of feet in soft beige socks on a bed"></div>
  <h3 class="blog-title">CONSECTETUR ADIPISCING ELIT DO EIUSMOD</h3>
  <p class="blog-text">Lorem ipsum dolor sit amet, consectetur adipiscing elit, sed do eiusmod tempor incididunt ut labore et dolore</p>
  <div class="blog-rule"></div>
  <div class="blog-meta"><span>by John doe</span><b>More information</b></div>
</article>

<!-- partners -->
<div class="abs partner-band"></div>
<h2 class="section-title partner-title" style="top:3110px">OUR PARTNER LOGO</h2>
<div class="abs badge" style="top:3200px;left:158px"></div>
<div class="abs badge" style="top:3200px;left:345px"></div>
<div class="abs badge" style="top:3200px;left:532px"></div>
<div class="abs badge" style="top:3200px;left:719px"></div>
<div class="abs badge" style="top:3200px;left:906px"></div>
<div class="abs badge" style="top:3320px;left:253px"></div>
<div class="abs badge" style="top:3320px;left:440px"></div>
<div class="abs badge" style="top:3320px;left:627px"></div>
<div class="abs badge" style="top:3320px;left:814px"></div>

<!-- footer band -->
<svg class="abs" style="top:3490px;left:0" width="1200" height="603" viewBox="0 0 1200 603">
  <polygon points="0,20 300,120 600,40 900,120 1200,20 1200,603 0,603" fill="#050505"/>
  <polyline points="0,20 300,120 600,40 900,120 1200,20" fill="none" stroke="#fff" stroke-width="8"/>
</svg>
<h2 class="abs mail-title">JOIN OUR MAILING LIST</h2>
<div class="abs mail-field">Enter Email Here</div>
<div class="abs subscribe">SUBSCRIBE</div>
<div class="abs rule" style="top:3794px"></div>

<div class="abs brand" style="top:3860px;left:92px">
  <span class="brand-mark"></span><span class="brand-name" style="color:var(--white);font-size:36px">ORVEL TECH</span>
</div>

<div class="abs footer-head" style="left:387px">QUICK LINKS</div>
<ul class="abs footer-list" style="left:392px"><li>Home</li><li>Products</li><li>Reviews</li><li>Blog</li></ul>

<div class="abs footer-head" style="left:585px">LEGAL</div>
<ul class="abs footer-list" style="left:590px"><li>Privacy Policy</li><li>Terms &amp; Conditions</li><li>Contact Us</li><li>Cookie Policy</li></ul>

<div class="abs footer-head" style="left:810px">CONTACT US</div>
<div class="abs" style="top:3850px;left:815px;width:250px">
  <div class="contact-row"><svg width="10" height="13" viewBox="0 0 10 13"><path fill="#fff" d="M5 0a5 5 0 0 1 5 5c0 3.5-5 8-5 8S0 8.5 0 5a5 5 0 0 1 5-5zm0 3a2 2 0 1 0 0 4 2 2 0 0 0 0-4z"/></svg><span>48 Lorem ipsum dolor sit amet consectetur adipiscing.</span></div>
  <div class="contact-row" style="margin-top:6px"><svg width="12" height="12" viewBox="0 0 24 24"><path fill="#fff" d="M6.6 10.8a15 15 0 0 0 6.6 6.6l2.2-2.2a1 1 0 0 1 1-.25 11.4 11.4 0 0 0 3.6.6 1 1 0 0 1 1 1V20a1 1 0 0 1-1 1A17 17 0 0 1 3 4a1 1 0 0 1 1-1h3.5a1 1 0 0 1 1 1c0 1.25.2 2.45.6 3.6a1 1 0 0 1-.25 1z"/></svg><span>555 210 4477</span></div>
  <div class="contact-row" style="margin-top:12px"><svg width="13" height="10" viewBox="0 0 13 10"><rect width="13" height="10" rx="1" fill="#fff"/><path d="M1 1l5.5 4.5L12 1" fill="none" stroke="#050505" stroke-width="1.2"/></svg><span>hello@orveltech.com</span></div>
</div>

<div class="abs rule" style="top:3990px"></div>
<div class="abs foot-social"><i></i><i></i><i></i><i></i></div>
<p class="abs copyright">© Copyright 2021 <b>ORVEL TECH</b> &nbsp;&nbsp; | &nbsp;&nbsp; All Rights Reserved</p>

</body>
</html>
```